PROPERTY BROCHURE

Need an attractive layout and design for this multi-page brochure

Industry/Entity Type

Real Estate Development

Colors

Designer to choose colors to be used in the design.

```html
<!DOCTYPE html>
<html lang="en">
<head>
<meta charset="utf-8">
<title>Property Brochure Spreads</title>
<link rel="stylesheet" href="https://fonts.googleapis.com/css2?family=Open+Sans:wght@300;400;600;700;800&display=swap">
<style>
:root{
  --bg:#2a2a2a;
  --ink:#1d1d1d;
  --muted:#555;
  --page:#ffffff;
  --page-shade:#ececec;
  --rule:#222;
  --green:#5aab1e;
  --navy:#1f2a3a;
  --table-line:#d6d6d6;
}
*{box-sizing:border-box;margin:0;padding:0}
html,body{width:1200px;height:882px;overflow:hidden;background:var(--bg);font-family:'Open Sans',Arial,sans-serif;color:var(--ink)}
.spread{position:absolute;width:530px;height:374px;background:linear-gradient(90deg,var(--page-shade) 0%,var(--page) 40%,var(--page) 50%,#f4f4f4 50%,var(--page) 80%);overflow:hidden}
.spread--intro{left:45px;top:38px}
.spread--city{left:616px;top:38px}
.spread--suburb{left:45px;top:462px}
.spread--demo{left:616px;top:462px}
.spread::after{content:"";position:absolute;left:265px;top:0;width:1px;height:100%;background:rgba(0,0,0,.06)}
.abs{position:absolute}
.title{font-size:10px;font-weight:300;letter-spacing:.2px;text-transform:uppercase;white-space:nowrap}
.title b{font-weight:700}
.rule{height:2px;background:var(--rule)}
.body{font-size:4.6px;line-height:1.55;color:var(--muted);text-align:justify}
.body p+p{margin-top:5px}
.photo{position:absolute}
.summary{font-size:9.5px;font-weight:300}
.summary b{font-weight:700}
.summary .row{position:absolute;left:0;white-space:nowrap}
.summary .val{position:absolute;left:118px;font-weight:400}
table{border-collapse:collapse;width:100%}
.pop td,.pop th{font-size:5px;height:11.6px;border-bottom:1px solid var(--table-line);padding-left:10px;text-align:left}
.pop th{font-weight:700}
.pop td:first-child{font-weight:700;background:#f1f1f1}
.demo-table td{font-size:5.5px;font-weight:600;height:13.6px;border:1px solid var(--table-line);padding-left:12px}
.demo-table td:last-child{width:17px;background:#f6f6f6;padding-left:12px;width:46px}
.fact{background:#ededed;border-left:0;padding:4px 7px}
.fact h3{font-size:9px;font-weight:800;line-height:1.1}
.fact span{font-size:7.5px;font-weight:600}
.card{position:absolute;background:linear-gradient(180deg,#fff,#f2f2f2);}
.card h4{position:absolute;font-size:5px;font-weight:600;text-transform:uppercase;text-align:center;width:64px;padding-bottom:4px;border-bottom:1.5px solid #333}
.big-green{font-size:13px;font-weight:700;color:var(--green)}
.occ{position:absolute;left:10px;font-size:8px;color:#333}
.occ small{position:absolute;left:30px;top:2px;font-size:3.6px;white-space:nowrap}
.occ i{position:absolute;left:0;top:11px;width:60px;height:1.5px;background:#ccc}
.occ i::before{content:"";position:absolute;left:0;top:0;height:100%;width:var(--w);background:var(--green)}
</style>
</head>
<body>

<section class="spread spread--intro">
  <h1 class="title abs" style="left:29px;top:27px">Property Development <b>Investment</b></h1>
  <div class="abs" style="left:29px;top:44px;font-size:7.5px">Project Summary</div>
  <div class="rule abs" style="left:29px;top:61px;width:77px"></div>
  <div class="summary abs" style="left:29px;top:82px;width:220px">
    <div class="row" style="top:0">Indicative <b>Return:</b><span class="val">43%</span></div>
    <div class="row" style="top:17px">Minimun <b>Term:</b><span class="val">12 months</span></div>
    <div class="row" style="top:34px">Minimun <b>Investment:</b><span class="val">$250,000</span></div>
  </div>
  <div class="photo" role="img" aria-label="Sketch of a two-storey house becoming a finished home, framed by two hands" style="left:35px;top:134px;width:495px;height:240px;background:radial-gradient(ellipse at 60% 55%,#c9ced6 0%,#e3e5e8 45%,rgba(255,255,255,0) 75%)"></div>
  <h2 class="title abs" style="left:294px;top:27px"><b>What we do</b></h2>
  <div class="rule abs" style="left:294px;top:44px;width:77px"></div>
  <div class="body abs" style="left:294px;top:59px;width:201px">
    <p>Granite Crest is a real estate development organisation that identifies and executes projects in metropolitan area of Melbourne. This projects offer investors the opportunity to obtain significant returns on investment above bank interest rates.</p>
    <p>Granite Crest is committed to providing quality medium density accommodation solutions to address the housing shortage currently experienced by the Australian and New Zealand market.</p>
    <p>Our projects represent a seamless balance between the financial requirements of our investors and the housing needs of those living in the communities we touch.</p>
  </div>
</section>

<section class="spread spread--city">
  <h1 class="title abs" style="left:29px;top:27px">Melbourne, <b>Victoria</b></h1>
  <div class="rule abs" style="left:29px;top:44px;width:77px"></div>
  <div class="body abs" style="left:29px;top:59px;width:200px">
    <p>Population growth in Melbourne is the strongest in the country at 3.2% over the year to June 2016 and is being driven by both strong overseas and interstate migration. Interstate migration increased 64% year-on-year (y-y) to June 2016 according to the State Statistics Office. By the middle of this century it will overtake Sydney to be Australia's largest city.</p>
  </div>
  <div class="abs" style="left:29px;top:114px;width:152px">
    <table class="pop">
      <tr><th>YEAR</th><th>POPULATION</th><th>GROWTH RATE</th></tr>
      <tr><td>2011</td><td>3850000</td><td>n/a</td></tr>
      <tr><td>2012</td><td>4090000</td><td>5.87%</td></tr>
      <tr><td>2013</td><td>4180000</td><td>2.20%</td></tr>
      <tr><td>2014</td><td>4250000</td><td>1.67%</td></tr>
      <tr><td>2015</td><td>4530000</td><td>6.60%</td></tr>
      <tr><td>2016</td><td>4670000</td><td>2.98%</td></tr>
      <tr><td>2017</td><td>4820000</td><td>3.21%</td></tr>
    </table>
  </div>
  <div class="body abs" style="left:295px;top:30px;width:199px">
    <p>Victoria is Australia's top performing economy. The annual state statistics measure of gross state domestic product puts Victoria's economic growth at 3.3 per cent throughout 2016-17.</p>
    <p>Since the 2014, over 200,000 jobs have been created, which equates to more than 250 new jobs every day. In the year to March 2017, average employment grew by 3.4%</p>
  </div>
  <div class="photo" role="img" aria-label="Photo of a modern angular public square building under blue sky" style="left:295px;top:86px;width:199px;height:125px;background:linear-gradient(180deg,#3f7fd0 0%,#8fb0cf 45%,#9a9286 75%,#b7a58a 100%)"></div>
  <div class="photo" role="img" aria-label="Photo of a river city skyline and observation wheel at dusk" style="left:29px;top:227px;width:310px;height:125px;background:linear-gradient(180deg,#4d6f9c 0%,#8fa4bd 45%,#3a4558 60%,#1f2c40 100%)"></div>
  <div class="photo" role="img" aria-label="Photo of city towers and a river bridge at twilight" style="left:348px;top:227px;width:182px;height:125px;background:linear-gradient(180deg,#2b4f8a 0%,#5f7fae 50%,#6b5a4a 75%,#3a4a5a 100%)"></div>
</section>

<section class="spread spread--suburb">
  <h1 class="title abs" style="left:29px;top:27px">Target Suburb: <b>Dandenong North</b></h1>
  <div class="body abs" style="left:29px;top:58px;width:198px">
    <p>Just under 30km from Melbourne's CBD, Dandenong North is a suburb home to over 22,000 people living in 9040 homes. The suburb in Melbourne's south east is still relatively affordable, with its median house price only just north of $610,000.</p>
    <p>That's not to say Dandenong North hasn't seen strong growth in recent years, as the median house price has jumped 17% over the past 12 months. In the past three years prices have increased 30%.</p>
  </div>
  <div class="photo" role="img" aria-label="Street map of the suburb with orange freeways crossing green land" style="left:30px;top:125px;width:198px;height:160px;background:linear-gradient(135deg,#e9efb0 0%,#f3f0c8 50%,#cfe4a2 100%)"></div>
  <div class="body abs" style="left:29px;top:296px;width:198px">
    <p>It's easy to see why the suburb has been performing well recently. The Monash and EastLink freeways provide easy access to the rest of Melbourne from Dandenong North, and the suburb is serviced by a number of private and public healthcare facilities.</p>
    <p>There are also multiple schools nearby and entertainment options such as the Larkfield Racecourse.</p>
  </div>
  <div class="body abs" style="left:294px;top:29px;width:201px">
    <p>Overall Dandenong North is a high demand market, with an average of 847 visits per property reported at <b style="color:#111">homeviewer.com.au</b> and currently, houses are only spending 23 days on the market.</p>
  </div>
  <svg class="abs" style="left:294px;top:62px" width="201" height="68" viewBox="0 0 201 68" aria-label="Line chart of median house price, 2010 to 2017">
    <g font-size="3" fill="#777" font-family="Open Sans,sans-serif">
      <text x="0" y="5">$800K</text><text x="0" y="21">$600K</text><text x="0" y="37">$400K</text><text x="0" y="53">$200K</text>
      <text x="56" y="60">2011</text><text x="80" y="60">2012</text><text x="104" y="60">2013</text><text x="128" y="60">2014</text><text x="152" y="60">2015</text><text x="176" y="60">2016</text><text x="194" y="60">2017</text>
    </g>
    <g stroke="#e4e4e4" stroke-width=".5"><line x1="14" y1="4" x2="200" y2="4"/><line x1="14" y1="20" x2="200" y2="20"/><line x1="14" y1="36" x2="200" y2="36"/><line x1="14" y1="52" x2="200" y2="52"/></g>
    <polyline fill="none" stroke="#e9a77f" stroke-width=".8" points="14,34 56,33 80,32 104,32 128,30 152,27 176,22 198,14"/>
    <polyline fill="none" stroke="#f2c9b0" stroke-width=".6" points="14,40 56,40 80,39 104,39 128,38 152,36 176,33 198,28"/>
    <rect x="14" y="55" width="20" height="6" fill="none" stroke="#ccc" stroke-width=".4"/>
    <rect x="82" y="63" width="34" height="5" fill="none" stroke="#ccc" stroke-width=".4"/>
  </svg>
  <div class="photo" role="img" aria-label="Photo of a suburban shopping street with parked cars and traffic" style="left:294px;top:144px;width:236px;height:206px;background:linear-gradient(180deg,#c7d3e0 0%,#aab0b3 40%,#7d7a74 65%,#55575a 100%)"></div>
</section>

<section class="spread spread--demo">
  <h1 class="title abs" style="left:29px;top:27px"><b>Demographics</b></h1>
  <div class="rule abs" style="left:29px;top:44px;width:80px"></div>
  <div class="abs" style="left:29px;top:54px;width:199px">
    <table class="demo-table">
      <tr><td>Total population</td><td>21910</td></tr>
      <tr><td>Median household income ($/weekly)</td><td>1031</td></tr>
      <tr><td>Median age of persons</td><td>37</td></tr>
      <tr><td>Median housing loan repayment ($/monthly)</td><td>1517</td></tr>
      <tr><td>Average household size</td><td>2.8</td></tr>
    </table>
  </div>

  <div class="card" style="left:29px;top:144px;width:157px;height:90px">
    <h4 style="left:10px;top:10px">Average age</h4>
    <h4 style="left:83px;top:10px">Dependency</h4>
    <div class="big-green abs" style="left:20px;top:50px">20 - 39</div>
    <svg class="abs" style="left:93px;top:32px" width="50" height="50" viewBox="0 0 50 50" aria-label="Donut chart: 51% singles, 49% families">
      <circle cx="25" cy="25" r="19" fill="none" stroke="var(--navy)" stroke-width="5"/>
      <circle cx="25" cy="25" r="19" fill="none" stroke="var(--green)" stroke-width="5" stroke-dasharray="60.9 119.4" transform="rotate(-90 25 25)"/>
      <text x="25" y="24" font-size="7" text-anchor="middle" fill="var(--green)" font-weight="600" font-family="Open Sans,sans-serif">51%</text>
      <text x="25" y="32" font-size="7" text-anchor="middle" fill="var(--navy)" font-weight="600" font-family="Open Sans,sans-serif">49%</text>
      <text x="3" y="27" font-size="2.6" fill="#fff" font-family="Open Sans,sans-serif">Singles</text>
      <text x="40" y="27" font-size="2.6" fill="#fff" font-family="Open Sans,sans-serif">Families</text>
    </svg>
  </div>

  <div class="card" style="left:29px;top:245px;width:157px;height:92px">
    <h4 style="left:10px;top:10px">Occupation</h4>
    <h4 style="left:83px;top:10px">Ownership</h4>
    <div class="occ" style="top:32px">20%<small>Manufacturing</small><i style="--w:22%"></i></div>
    <div class="occ" style="top:48px">11%<small>Retail trade</small><i style="--w:12%"></i></div>
    <div class="occ" style="top:64px">11%<small>Health Care/Social</small><i style="--w:12%"></i></div>
    <svg class="abs" style="left:93px;top:32px" width="50" height="50" viewBox="0 0 50 50" aria-label="Donut chart: 36% fully owned, 35% renting, 29% purchasing">
      <circle cx="25" cy="25" r="19" fill="none" stroke="#c8c8c8" stroke-width="5"/>
      <circle cx="25" cy="25" r="19" fill="none" stroke="var(--green)" stroke-width="5" stroke-dasharray="43 119.4" transform="rotate(-90 25 25)"/>
      <circle cx="25" cy="25" r="19" fill="none" stroke="var(--navy)" stroke-width="5" stroke-dasharray="0 43 34.6 119.4" transform="rotate(-90 25 25)"/>
      <text x="25" y="20" font-size="6" text-anchor="middle" fill="var(--green)" font-weight="600" font-family="Open Sans,sans-serif">36%</text>
      <text x="25" y="27" font-size="6" text-anchor="middle" fill="var(--navy)" font-weight="600" font-family="Open Sans,sans-serif">35%</text>
      <text x="25" y="34" font-size="6" text-anchor="middle" fill="#aaa" font-weight="600" font-family="Open Sans,sans-serif">29%</text>
    </svg>
  </div>

  <div class="fact abs" style="left:294px;top:28px;width:74px"><h3>MEDIAN RENTAL PRICE</h3><span>$350 per week</span></div>
  <div class="fact abs" style="left:294px;top:69px;width:74px"><h3>NUMBER OF RENTALS</h3><span>446</span></div>
  <div class="body abs" style="left:294px;top:113px;width:210px;text-align:left">
    <p>Based on recorded House and Unit rentals within the last 12 months (2017)<br>Based on a rolling 12 month period and may differ from calendar year statistics</p>
  </div>
  <div class="photo" role="img" aria-label="Photo of a leafy residential street with a speed limit 10 sign" style="left:204px;top:142px;width:326px;height:194px;background:linear-gradient(180deg,#dfe8ef 0%,#8fae6a 35%,#4f7a3a 65%,#9a9b98 100%)"></div>
</section>

</body>
</html>
```